Corvenix Business Card

Our mission is to craft high value solutions combining consulting and edge technologies for helping big and middle sized companies in the Digital Transformation Process that they must face. We think that this transformation will impact business processes and people skills in a new manner. Corvenix's value proposition is to collaborate with our clients for creating new competitive advantages based on technology, processes and people.
We already have a logo designed through your platform.

Industry/Entity Type

Business

```html
<!DOCTYPE html>
<html lang="en">
<head>
<meta charset="utf-8">
<title>Corvenix Business Card</title>
<link rel="stylesheet" href="https://fonts.googleapis.com/css2?family=Jost:wght@400;500&family=Crimson+Pro:wght@400&display=swap">
<style>
  :root {
    --frame: #2f93d1;
    --page: #ffffff;
    --card-dark: #231f20;
    --card-light: #fdfcf0;
    --brand-blue: #1e8fd6;
    --ink: #333333;
    --ink-soft: #6b6b6b;
    --on-dark: #ffffff;
    --trace: #d8ecee;
  }
  * { box-sizing: border-box; margin: 0; padding: 0; }
  html, body { width: 1200px; height: 782px; overflow: hidden; background: var(--page); }
  .board {
    position: relative; width: 1200px; height: 782px;
    border: 2px solid var(--frame); background: var(--page);
  }
  .card {
    position: absolute; width: 466px; height: 286px;
    border-radius: 14px 22px 14px 14px;
    box-shadow: 3px 5px 10px rgba(0,0,0,0.28);
  }
  .card--front { background: var(--card-dark); left: 106px; }
  .card--back { background: var(--card-light); left: 612px; }
  .row-1 { top: 95px; }
  .row-2 { top: 409px; }

  .brand { position: absolute; display: flex; align-items: center; }
  .brand__dot { border-radius: 50%; background: var(--brand-blue); flex: none; }
  .brand__name {
    font-family: "Jost", sans-serif; font-weight: 500; letter-spacing: 1px;
  }
  .card--front .brand { left: 82px; top: 97px; gap: 18px; }
  .card--front .brand__dot { width: 86px; height: 86px; }
  .card--front .brand__name { color: var(--on-dark); font-size: 38px; }
  .card--back .brand__name { color: var(--ink); font-size: 21px; }

  .website {
    position: absolute; left: 0; right: 0; bottom: 22px; text-align: center;
    font-family: "Jost", sans-serif; font-size: 14px; letter-spacing: 1.4px; color: var(--on-dark);
  }

  .traces {
    position: absolute; left: 0; top: 70px; width: 466px; height: 216px;
    border-radius: 0 0 14px 14px;
    background: linear-gradient(100deg, rgba(216,236,238,0) 0%, rgba(216,236,238,0.55) 45%, rgba(200,230,236,0.35) 100%);
  }

  .contact { position: absolute; font-family: "Crimson Pro", serif; }
  .contact__name { font-size: 22px; color: var(--ink); padding: 0 0 2px 16px; }
  .contact__role { font-size: 13px; color: var(--ink-soft); letter-spacing: 0.6px; padding-left: 16px; margin-top: 4px; }
  .contact__line {
    display: flex; align-items: center; gap: 8px;
    font-size: 13px; letter-spacing: 0.8px; color: var(--ink); padding-left: 18px;
  }
  .contact__line svg { width: 12px; height: 12px; fill: var(--brand-blue); flex: none; }
  .contact__list { margin-top: 14px; display: flex; flex-direction: column; gap: 6px; }

  .layout-a .brand { left: 28px; top: 38px; gap: 10px; }
  .layout-a .brand__dot { width: 40px; height: 40px; }
  .layout-a .contact { left: 220px; top: 142px; }
  .layout-a .contact__name { border-bottom: 1px solid var(--ink); width: 208px; }

  .layout-b .divider { position: absolute; left: 222px; top: 56px; width: 2px; height: 186px; background: var(--brand-blue); }
  .layout-b .brand { left: 34px; top: 124px; gap: 10px; }
  .layout-b .brand__dot { width: 38px; height: 38px; }
  .layout-b .contact { left: 226px; top: 118px; }
  .layout-b .contact__name { border-bottom: 1px solid var(--brand-blue); width: 194px; }
</style>
</head>
<body>
<main class="board">
  <section class="card card--front row-1">
    <div class="brand"><span class="brand__dot"></span><span class="brand__name">CORVENIX</span></div>
    <p class="website">www.corvenix.com</p>
  </section>

  <section class="card card--back row-1 layout-a">
    <div class="traces" role="img" aria-label="Faint circuit-trace pattern of lines ending in dots"></div>
    <div class="brand"><span class="brand__dot"></span><span class="brand__name">CORVENIX</span></div>
    <div class="contact">
      <p class="contact__name">Mr. Daniel Mercer</p>
      <p class="contact__role">manager</p>
      <div class="contact__list">
        <p class="contact__line"><svg viewBox="0 0 24 24"><path d="M6.6 10.8a15.1 15.1 0 0 0 6.6 6.6l2.2-2.2a1 1 0 0 1 1-.25 11.4 11.4 0 0 0 3.6.57 1 1 0 0 1 1 1V20a1 1 0 0 1-1 1A17 17 0 0 1 3 4a1 1 0 0 1 1-1h3.5a1 1 0 0 1 1 1c0 1.25.2 2.45.57 3.57a1 1 0 0 1-.25 1z"/></svg>372.614.809</p>
        <p class="contact__line"><svg viewBox="0 0 24 24"><path d="M2 5h20v14H2z M2 5l10 8 10-8" /><path d="M2 5l10 8 10-8v2l-10 8L2 7z" fill="#fdfcf0"/></svg>daniel.mercer@mailbox.com</p>
      </div>
    </div>
  </section>

  <section class="card card--front row-2">
    <div class="brand"><span class="brand__dot"></span><span class="brand__name">CORVENIX</span></div>
    <p class="website">www.corvenix.com</p>
  </section>

  <section class="card card--back row-2 layout-b">
    <div class="brand"><span class="brand__dot"></span><span class="brand__name">CORVENIX</span></div>
    <span class="divider"></span>
    <div class="contact">
      <p class="contact__name">Mr. Daniel Mercer</p>
      <p class="contact__role">manager</p>
      <div class="contact__list">
        <p class="contact__line"><svg viewBox="0 0 24 24"><path d="M6.6 10.8a15.1 15.1 0 0 0 6.6 6.6l2.2-2.2a1 1 0 0 1 1-.25 11.4 11.4 0 0 0 3.6.57 1 1 0 0 1 1 1V20a1 1 0 0 1-1 1A17 17 0 0 1 3 4a1 1 0 0 1 1-1h3.5a1 1 0 0 1 1 1c0 1.25.2 2.45.57 3.57a1 1 0 0 1-.25 1z"/></svg>372.614.809</p>
        <p class="contact__line"><svg viewBox="0 0 24 24"><path d="M2 5h20v14H2z"/><path d="M2 5l10 8 10-8v2l-10 8L2 7z" fill="#fdfcf0"/></svg>daniel.mercer@mailbox.com</p>
      </div>
    </div>
  </section>
</main>
</body>
</html>
```